Slim Can Designs! Single Origin Coffee Cold Brew Coffee Cans

Amber Heron is a lifestyle brand with a focus on producing coffee. We need a three labels designed for our Cold Brew Cans. These will be 12 oz. slim cans for cold brew coffee. Each can will represent a different flavor profile tied to a virtue. Template Attached. We only have three products for cold brew cans. Please also review all the files included in our project for reference.
1. Harmony : Toffee, Smokey, Chocolate
Things to include: Single Origin Coffee Dark Roast / Bold and Strong
2. Courage : Caramel, Chocolate, Dried Mango / Bright and Sparkling
Things to include: Single Origin Coffee Medium Roast
3. Honesty : Berry, Citrus, Floral / Smooth and Rich
Things to include: Single Origin Coffee Light Roast
All cans should include:
1. our logo. and brand colors.
2. all virtue icons if possible ?
3. Nutrition Label attached. Use this for all three, it may change but please use for placeholder.
4. Barcode
5. Net wt. 12oz
6. Ingredients : Single Origin Coffee, Water
7. BE KIND DRINK COFFEE
8. EST 2012
9. Roasted in Portland
10. Our business name and address:
Amber Heron Coffee Roasters
Portland, Oregon
web amberheronco.com
instagram amberheronco
11. Ethically Sourced Coffee Icon: if you can create one
12. Please recycle icon
13. Shake Lightly and Serve Chilled
14. Caffeine Content 200mg. : this might change between product but please use this as a placeholder for now.
15.

These designs should be cohesive and have some connection to our other brand element to tie together with our other current product designs. We are looking for sleek but fun and bold with colors and elements.

Target Market(s)

Mass market

Industry/Entity Type

Coffee

Font styles to use
Sans Serif
Other font styles liked:
• Please refer to our brand kit

Requirements
Must have
• Please refer to description
Nice to have

```html
<!DOCTYPE html>
<html lang="en">
<head>
<meta charset="utf-8">
<title>Amber Heron Cold Brew Labels</title>
<link href="https://fonts.googleapis.com/css2?family=Oswald:wght@700&family=Montserrat:wght@300;500;600;700&display=swap" rel="stylesheet">
<style>
  :root{
    --navy:#1e3a5c;
    --navy-deep:#17304d;
    --silver-light:#f4f5f7;
    --silver-mid:#d9dce0;
    --silver-dark:#b9bdc3;
    --gold:#e6bf8c;
    --teal:#5e978a;
    --red:#c84a5f;
    --page:#e9eaec;
    --white:#ffffff;
  }
  *{box-sizing:border-box;margin:0;padding:0}
  html,body{width:1200px;height:1097px;overflow:hidden}
  body{
    background:var(--page);
    font-family:"Montserrat",sans-serif;
    display:flex;
    justify-content:center;
    align-items:center;
    gap:60px;
  }
  .label{
    position:relative;
    width:300px;
    height:750px;
    border-radius:14px;
    overflow:hidden;
    background:var(--navy);
    color:var(--navy);
  }
  .label--courage{--accent:var(--gold)}
  .label--harmony{--accent:var(--teal)}
  .label--honesty{--accent:var(--red)}

  .top-band{
    position:absolute;left:0;right:0;top:0;height:255px;
    background:linear-gradient(90deg,var(--navy-deep),var(--navy) 50%,var(--navy-deep));
  }
  .stripe{position:absolute;left:0;right:0;height:5px;background:var(--accent)}
  .stripe--top{top:68px}
  .stripe--bottom{top:650px}

  .brand{
    position:absolute;left:0;right:0;top:112px;
    text-align:center;color:var(--white);
  }
  .brand-mark{
    width:34px;height:34px;border-radius:50%;
    background:var(--white);margin:0 auto 12px;
  }
  .brand-name{
    font-weight:300;font-size:17px;line-height:1.05;letter-spacing:.5px;
    text-transform:uppercase;
  }
  .brand-tag{
    font-weight:300;font-size:7.5px;letter-spacing:3px;margin-top:3px;
  }
  .est{
    position:absolute;left:50%;top:222px;transform:translateX(-50%);
    display:flex;align-items:center;gap:6px;
  }
  .est-line{width:62px;height:2px;background:var(--accent)}
  .est-pill{
    background:var(--accent);color:var(--navy);
    font-size:8px;font-weight:500;padding:3px 9px;border-radius:8px;
    white-space:nowrap;line-height:1;
  }
  .label--harmony .est-pill,.label--honesty .est-pill{color:var(--white)}

  .body{
    position:absolute;left:0;right:0;top:255px;height:395px;
    background:linear-gradient(90deg,var(--silver-dark),var(--silver-light) 35%,var(--silver-mid) 70%,var(--silver-dark));
  }
  .virtue{
    font-family:"Oswald",sans-serif;font-weight:700;
    font-size:58px;line-height:1;text-align:center;
    margin-top:22px;letter-spacing:-.5px;white-space:nowrap;
  }
  .notes{
    display:flex;align-items:center;gap:12px;
    margin:22px 0 0 42px;
  }
  .note-icon{width:48px;height:48px;border-radius:50%;background:var(--accent);flex:none}
  .note-list{list-style:none;font-size:14px;font-weight:500;line-height:1.3;letter-spacing:.3px}
  .origin-art{
    width:190px;height:72px;margin:20px auto 0;
    background:linear-gradient(120deg,var(--navy) 0%,#3a5877 35%,#d9b8a8 55%,var(--navy) 80%);
  }
  .roast{
    width:236px;margin:14px auto 0;
    background:var(--navy);color:var(--white);
    font-weight:700;font-size:15px;text-align:center;
    padding:4px 0;border-radius:14px;letter-spacing:.3px;white-space:nowrap;
  }
  .origin-row{
    display:flex;align-items:center;justify-content:center;gap:18px;
    margin-top:14px;
  }
  .sourced-badge{
    width:36px;height:36px;border-radius:50%;
    border:2px solid var(--navy);background:var(--silver-light);
  }
  .roasted{font-size:12px;font-weight:600;line-height:1.35;text-align:center}

  .net{
    position:absolute;left:0;right:0;top:690px;
    text-align:center;color:var(--white);font-size:10px;font-weight:500;
  }
</style>
</head>
<body>

  <section class="label label--courage">
    <div class="top-band"></div>
    <div class="stripe stripe--top"></div>
    <div class="brand">
      <div class="brand-mark"></div>
      <p class="brand-name">Amber Heron<br>Coffee Roasters</p>
      <p class="brand-tag">SINGLE ORIGIN COFFEE</p>
    </div>
    <div class="est"><span class="est-line"></span><span class="est-pill">EST 2012</span><span class="est-line"></span></div>
    <div class="body">
      <h2 class="virtue">COURAGE</h2>
      <div class="notes">
        <div class="note-icon" role="img" aria-label="Courage virtue icon"></div>
        <ul class="note-list"><li>CARAMEL</li><li>CHOCOLATE</li><li>DRIED MANGO</li></ul>
      </div>
      <div class="origin-art" role="img" aria-label="Single Origin Coffee lettering on a swirl pattern"></div>
      <p class="roast">MEDIUM ROAST</p>
      <div class="origin-row">
        <div class="sourced-badge"></div>
        <p class="roasted">Roasted in<br>Portland</p>
      </div>
    </div>
    <div class="stripe stripe--bottom"></div>
    <p class="net">Net Weight: 12 oz.</p>
  </section>

  <section class="label label--harmony">
    <div class="top-band"></div>
    <div class="stripe stripe--top"></div>
    <div class="brand">
      <div class="brand-mark"></div>
      <p class="brand-name">Amber Heron<br>Coffee Roasters</p>
      <p class="brand-tag">SINGLE ORIGIN COFFEE</p>
    </div>
    <div class="est"><span class="est-line"></span><span class="est-pill">EST 2012</span><span class="est-line"></span></div>
    <div class="body">
      <h2 class="virtue">HARMONY</h2>
      <div class="notes">
        <div class="note-icon" role="img" aria-label="Harmony virtue icon"></div>
        <ul class="note-list"><li>TOFFEE</li><li>SMOKEY</li><li>CHOCOLATE</li></ul>
      </div>
      <div class="origin-art" role="img" aria-label="Single Origin Coffee lettering on a swirl pattern"></div>
      <p class="roast">BOLD AND STRONG</p>
      <div class="origin-row">
        <div class="sourced-badge"></div>
        <p class="roasted">Roasted in<br>Portland</p>
      </div>
    </div>
    <div class="stripe stripe--bottom"></div>
    <p class="net">Net Weight: 12 oz.</p>
  </section>

  <section class="label label--honesty">
    <div class="top-band"></div>
    <div class="stripe stripe--top"></div>
    <div class="brand">
      <div class="brand-mark"></div>
      <p class="brand-name">Amber Heron<br>Coffee Roasters</p>
      <p class="brand-tag">SINGLE ORIGIN COFFEE</p>
    </div>
    <div class="est"><span class="est-line"></span><span class="est-pill">EST 2012</span><span class="est-line"></span></div>
    <div class="body">
      <h2 class="virtue">HONESTY</h2>
      <div class="notes">
        <div class="note-icon" role="img" aria-label="Honesty virtue icon"></div>
        <ul class="note-list"><li>BERRY</li><li>CITRUS</li><li>FLORAL</li></ul>
      </div>
      <div class="origin-art" role="img" aria-label="Single Origin Coffee lettering on a swirl pattern"></div>
      <p class="roast">LIGHT ROAST</p>
      <div class="origin-row">
        <div class="sourced-badge"></div>
        <p class="roasted">Roasted in<br>Portland</p>
      </div>
    </div>
    <div class="stripe stripe--bottom"></div>
    <p class="net">Net Weight: 12 oz.</p>
  </section>

</body>
</html>
```